Brevin Law Client Handbook

We are a small, rapidly growing, criminal defense law firm located in a suburb of Seattle, WA. The cover should be professional and be consistent with our image a sleek, modern, and efficient. The included files show our designs used in other projects for reference.

```html
<!DOCTYPE html>
<html lang="en">
<head>
<meta charset="utf-8">
<title>Brevin Law Firm — Client Handbook Cover</title>
<link rel="stylesheet" href="https://fonts.googleapis.com/css2?family=Cinzel:wght@400&family=Montserrat:wght@300;400&family=Roboto:wght@300&display=swap">
<style>
  :root {
    --navy: #0c2b53;
    --navy-deep: #0a2447;
    --navy-soft: #153a66;
    --white: #ffffff;
    --rule: #8796ab;
    --photo-light: #6c83a3;
    --photo-mid: #2e4b74;
  }
  * { margin: 0; padding: 0; box-sizing: border-box; }
  html, body { width: 1200px; height: 872px; overflow: hidden; background: var(--navy); }
  .cover {
    position: relative;
    width: 1200px; height: 872px;
    background: var(--navy);
    color: var(--white);
    overflow: hidden;
  }
  .courthouse-photo {
    position: absolute; left: 0; top: 70px; width: 760px; height: 700px;
    background: radial-gradient(ellipse at 45% 45%, var(--navy-soft) 0%, var(--navy) 70%);
    opacity: .8;
  }
  .statue-photo {
    position: absolute; left: 670px; top: 94px; width: 515px; height: 656px;
    background: radial-gradient(ellipse at 55% 40%, var(--photo-light) 0%, var(--photo-mid) 45%, var(--navy) 85%);
    border-radius: 40% 40% 10% 10%;
    opacity: .85;
  }

  /* Back cover */
  .back-title {
    position: absolute; left: 0; width: 590px; top: 148px; text-align: center;
    font-family: "Cinzel", serif; font-size: 84px; line-height: 1; letter-spacing: 1px;
  }
  .ruled-label {
    position: absolute; display: flex; align-items: center; justify-content: center;
    font-family: "Montserrat", sans-serif; font-weight: 300; letter-spacing: 1px;
  }
  .ruled-label::before, .ruled-label::after {
    content: ""; flex: 1; height: 1px; background: var(--rule);
  }
  .back-subtitle { left: 139px; width: 310px; top: 230px; font-size: 22px; gap: 14px; }
  .back-blurb {
    position: absolute; left: 81px; top: 286px; width: 427px;
    font-family: "Roboto", sans-serif; font-weight: 300; font-size: 14px;
    line-height: 31.5px; letter-spacing: .5px;
    text-align: justify; text-align-last: center;
  }
  .back-wordmark {
    position: absolute; left: 190px; top: 640px; width: 220px; text-align: center;
    font-family: "Cinzel", serif; font-size: 26px; letter-spacing: 6px; line-height: 1.3;
  }

  /* Spine */
  .spine-text {
    position: absolute; left: 586px; writing-mode: vertical-rl;
    font-family: "Cinzel", serif; font-size: 21px; letter-spacing: 3px; line-height: 1;
  }
  .spine-firm { top: 113px; }
  .spine-author { top: 502px; }
  .spine-mark {
    position: absolute; left: 585px; top: 413px; width: 34px; height: 45px;
    background: var(--white);
  }

  /* Front cover */
  .author-name {
    position: absolute; left: 680px; width: 464px; top: 45px; text-align: center;
    font-family: "Cinzel", serif; font-size: 35px; letter-spacing: 2px; line-height: 1;
  }
  .author-role {
    position: absolute; left: 680px; width: 464px; top: 89px; text-align: center;
    font-family: "Montserrat", sans-serif; font-weight: 400; font-size: 19px; letter-spacing: 2px;
  }
  .front-title {
    position: absolute; left: 670px; width: 484px; top: 652px; text-align: center;
    font-family: "Cinzel", serif; font-size: 118px; line-height: 1;
  }
  .front-subtitle { left: 679px; width: 465px; top: 766px; font-size: 34px; gap: 22px; }
</style>
</head>
<body>
<main class="cover">
  <div class="courthouse-photo" role="img" aria-label="Faint photograph of a columned courthouse facade"></div>
  <div class="statue-photo" role="img" aria-label="Photograph of a Lady Justice statue holding scales and a sword"></div>

  <section class="back-cover">
    <h2 class="back-title">BREVIN</h2>
    <div class="ruled-label back-subtitle">LAW FIRM</div>
    <p class="back-blurb">Lorem Ipsum is simply dummy text of the printing and typesetting industry. Lorem Ipsum has been the industry's standard dummy text ever since the 1500s, when an unknown printer took a galley of type and scrambled it to make a type specimen book. It has survived not only five centuries, but also the leap into electronic typesetting, remaining essentially unchanged. It was popularised in the 1960s with the release of Typeline sheets containing Lorem Ipsum passages, and more recently with desktop publishing software like Quillset Press including versions of Lorem Ipsum.</p>
    <div class="back-wordmark">BREVIN LAW FIRM</div>
  </section>

  <section class="spine">
    <span class="spine-text spine-firm">BREVIN LAW FIRM</span>
    <span class="spine-mark"></span>
    <span class="spine-text spine-author">DANIEL BREVIN</span>
  </section>

  <section class="front-cover">
    <p class="author-name">DANIEL BREVIN</p>
    <p class="author-role">ATTORNEY</p>
    <h1 class="front-title">BREVIN</h1>
    <div class="ruled-label front-subtitle">LAW FIRM</div>
  </section>
</main>
</body>
</html>
```